PowerPoint Design Project

We are looking for a corporate presentation design (example content provided on approximately 30 slides).

The design will be a corporate design for our brand: GVRU
Continental Voyage Planners Union
For brand colours, requirements and logo look at: www.gvru-sample.org/media
or check the attached documents. We need to incorporate logo and brand but we are happy to refresh the palette. Attached please also find designs and colour palette of our new website-presentation should complement these.

You are also free to use photos from events some of which can be found here:
http://www.socialpage-example.com/pages/Continental-Voyage-Planners-Union/507194362810935?sk=photos_stream

Most important:
-PROFESSIONAL AUDIENCE-PROFESSIONAL DESIGN
-SIMPLE (see example our homepage in attachment)
-ADDED SIMPLE ANIMATIONS

-DESIGN TO BE DONE ON THE EXAMPLE PRESENTATION BUT TO BE RE-USABLE FOR OTHER PRESENTATIONS
Updates

Hi, we have just uploaded our corporate social media icons which could be added on contact/end slide and on the welcome slide.

Hi all, 

-I uploaded a new high res version of the map which can be included in your designs (feel free to change colour scheme)
-Also amended upload of the Google + social media icon

Reason: I am looking forward to seeing a couple more designs. Please try including some suggested animations.

Target Market(s)

Presentation will be B2B and most audience are representatives of various companies in the tourism industry (tour operators, tourist boards, hotels )

Industry/Entity Type

Events

Requirements
Must have
• sleek graphics design
Nice to have
• animations

```html
<!DOCTYPE html>
<html lang="en">
<head>
<meta charset="utf-8">
<title>GVRU – Project Title</title>
<link rel="stylesheet" href="https://fonts.googleapis.com/css2?family=Carlito:wght@400;700&family=Roboto+Condensed:wght@700&display=swap">
<style>
  :root {
    --navy: #1c2a56;
    --ribbon: #0d1233;
    --white: #ffffff;
    --text: #1a1a1a;
    --grey-light: #f2f2f2;
    --grey-mid: #e2e2e2;
    --grey-dark: #d6d6d6;
    --rule: #8a93b3;
  }
  * { margin: 0; padding: 0; box-sizing: border-box; }
  html, body { width: 1200px; height: 900px; overflow: hidden; background: var(--white); }
  .slide {
    position: relative;
    width: 1200px;
    height: 900px;
    overflow: hidden;
    font-family: "Carlito", "Calibri", sans-serif;
    background: var(--white);
  }
  .slide__backdrop {
    position: absolute;
    left: 0; top: 210px;
    width: 1200px; height: 690px;
    background:
      linear-gradient(180deg, rgba(255,255,255,0) 0%, rgba(255,255,255,0) 78%, rgba(255,255,255,0.9) 100%),
      linear-gradient(90deg, var(--grey-mid) 0%, var(--grey-light) 22%, #fafafa 45%, var(--grey-light) 62%, var(--grey-mid) 80%, var(--grey-dark) 100%);
  }
  .slide__map {
    position: absolute;
    left: 660px; top: 215px;
    width: 540px; height: 630px;
    background: radial-gradient(ellipse at 65% 45%, rgba(200,200,200,0.55) 0%, rgba(215,215,215,0.3) 45%, rgba(230,230,230,0) 75%);
  }
  .slide__header {
    position: absolute;
    left: 0; top: 0;
    width: 1200px; height: 210px;
    background: var(--navy);
  }
  .slide__title {
    position: absolute;
    left: 390px; top: 88px;
    color: var(--white);
    font-size: 47px;
    font-weight: 400;
    letter-spacing: 0.5px;
    line-height: 1;
  }
  .ribbon {
    position: absolute;
    left: 90px; top: 0;
    width: 251px; height: 460px;
  }
  .ribbon__shape { position: absolute; inset: 0; }
  .ribbon__brand {
    position: absolute;
    left: 0; top: 96px;
    width: 251px;
    text-align: center;
    color: var(--white);
    font-family: "Carlito", "Calibri", sans-serif;
    font-weight: 400;
    font-size: 42px;
    letter-spacing: 2px;
    line-height: 1;
  }
  .intro {
    position: absolute;
    left: 390px; top: 462px;
    width: 640px;
    color: var(--text);
    font-size: 21px;
    line-height: 35px;
  }
  .footer__rule {
    position: absolute;
    left: 0; top: 819px;
    width: 1200px; height: 2px;
    background: var(--rule);
  }
  .footer__page {
    position: absolute;
    left: 36px; top: 843px;
    font-family: "Roboto Condensed", "Arial Narrow", sans-serif;
    font-weight: 700;
    font-size: 23px;
    color: var(--text);
  }
</style>
</head>
<body>
  <main class="slide">
    <div class="slide__backdrop" role="img" aria-label="Soft grey halftone dot texture"></div>
    <div class="slide__map" role="img" aria-label="Faint dotted map of Europe"></div>

    <header class="slide__header">
      <h1 class="slide__title">PROJECT TITLE HERE</h1>
    </header>

    <div class="ribbon">
      <svg class="ribbon__shape" width="251" height="460" viewBox="0 0 251 460" aria-hidden="true">
        <polygon points="0,0 251,0 251,408 0,460" fill="var(--ribbon)"/>
      </svg>
      <div class="ribbon__brand">GVRU</div>
    </div>

    <p class="intro">Some introduction content here Some introduction content hereSome introduction content hereSome introduction content here Some introduction content hereSome introduction content here</p>

    <footer>
      <div class="footer__rule"></div>
      <div class="footer__page">Page : 01</div>
    </footer>
  </main>
</body>
</html>
```